Super elegant, crisp & clean Business card design required

We recently upgraded our branding - which is on our website - tavorelstudio.com

I would like a simple, yet elegant, clean business card design please.

The font of my logo is Cinzel - and because of the natural colour - it's best to have this on a black background.

I would like to have the back of the business card - with simply my logo.

PLEASE DO NOT SUBMIT A COMPLICATED / UNCLEAN DESIGN

Industry/Entity Type

Business

Contact Information for Business Card

Dalvik Ostrander Photography

Font styles to use
Other font styles liked:
• Cinzel

Requirements
Must have
• A backpage with nothing but my logo
• Simple design - stands out
Should not have
• Colour that dont align with my logo
• Over complicated '/ non symmetrical design

```html
<!DOCTYPE html>
<html lang="en">
<head>
<meta charset="utf-8">
<title>Dalvik Ostrander Photography – Business Card</title>
<link rel="stylesheet" href="https://fonts.googleapis.com/css2?family=Cinzel:wght@400;500&family=Didact+Gothic&display=swap">
<style>
  :root {
    --stage: #161616;
    --card-black: #000000;
    --card-white: #ffffff;
    --gold: #8b7b63;
    --ink: #111111;
  }
  * { margin: 0; padding: 0; box-sizing: border-box; }
  html, body { width: 1200px; height: 741px; overflow: hidden; background: var(--stage); }
  .stage { position: relative; width: 1200px; height: 741px; }
  .card {
    position: absolute; top: 229px; width: 494px; height: 282px;
    border-radius: 16px; overflow: hidden;
  }
  .card--back { left: 99px; background: var(--card-black); }
  .card--front { left: 608px; background: var(--card-white); }

  .brand { position: absolute; text-align: center; color: var(--gold); font-family: "Cinzel", serif; font-weight: 400; }
  .brand__name { display: block; white-space: nowrap; }
  .brand__tag { display: block; letter-spacing: 0.55em; margin-right: -0.55em; }

  .card--back .brand { left: 0; right: 0; top: 174px; }
  .card--back .brand__name { font-size: 21px; }
  .card--back .brand__tag { font-size: 10.5px; margin-top: 2px; }

  .card--front .brand { left: 0; width: 238px; top: 153px; }
  .card--front .brand__name { font-size: 16.5px; }
  .card--front .brand__tag { font-size: 8.5px; margin-top: 1px; }

  .divider { position: absolute; left: 237px; top: 55px; width: 1px; height: 141px; background: var(--gold); }

  .person { position: absolute; left: 254px; top: 52px; }
  .person__name { font-family: "Cinzel", serif; font-size: 20px; color: var(--ink); line-height: 1; font-weight: 500; }
  .person__role { font-family: "Didact Gothic", sans-serif; font-size: 13px; color: var(--gold); margin-top: 1px; }

  .contacts { position: absolute; left: 255px; top: 145px; list-style: none; font-family: "Didact Gothic", sans-serif; font-size: 13px; color: var(--gold); }
  .contacts li { display: flex; align-items: center; height: 17.5px; }
  .contacts svg { width: 11px; height: 11px; margin-right: 8px; fill: var(--ink); }

  .wave { position: absolute; left: 0; bottom: 0; width: 494px; height: 282px; }
</style>
</head>
<body>
<main class="stage">
  <section class="card card--back" aria-label="Card back">
    <div class="brand">
      <span class="brand__name">Dalvik Ostrander</span>
      <span class="brand__tag">Photography</span>
    </div>
  </section>

  <section class="card card--front" aria-label="Card front">
    <svg class="wave" viewBox="0 0 600 342" preserveAspectRatio="none" aria-hidden="true">
      <path d="M0 266 C120 300 200 330 300 326 C420 320 500 270 600 262 L600 342 L0 342 Z" fill="var(--card-black)"/>
      <path d="M0 264 C120 296 200 324 300 320 C420 314 500 264 600 258 L600 262 C500 270 420 320 300 326 C200 330 120 300 0 266 Z" fill="var(--card-white)"/>
      <path d="M30 276 C140 312 220 324 320 314 C430 302 510 262 590 260 C510 258 430 282 320 300 C220 314 140 306 30 276 Z" fill="var(--gold)"/>
    </svg>

    <div class="brand">
      <span class="brand__name">Dalvik Ostrander</span>
      <span class="brand__tag">Photography</span>
    </div>

    <div class="divider"></div>

    <div class="person">
      <p class="person__name">CORIN HALE</p>
      <p class="person__role">Chief Executive Officer</p>
    </div>

    <ul class="contacts">
      <li><svg viewBox="0 0 24 24"><path d="M6.6 10.8a15 15 0 0 0 6.6 6.6l2.2-2.2a1 1 0 0 1 1-.25 11.4 11.4 0 0 0 3.6.57 1 1 0 0 1 1 1V20a1 1 0 0 1-1 1A17 17 0 0 1 3 4a1 1 0 0 1 1-1h3.5a1 1 0 0 1 1 1c0 1.25.2 2.45.57 3.57a1 1 0 0 1-.25 1z"/></svg>44 7700 900418</li>
      <li><svg viewBox="0 0 24 24"><path d="M2 5h20v14H2z M3.5 6.5 12 13l8.5-6.5" fill="var(--ink)" stroke="var(--card-white)" stroke-width="1.6"/></svg>do.photography@mailhaven.com</li>
      <li><svg viewBox="0 0 24 24"><circle cx="12" cy="12" r="10"/><path d="M2 12h20M12 2c3 3 3 17 0 20M12 2c-3 3-3 17 0 20" fill="none" stroke="var(--card-white)" stroke-width="1.4"/></svg>www.tavorelstudio.com</li>
    </ul>
  </section>
</main>
</body>
</html>
```